PDF-Dokumente für Vermietung und Verwaltung von Immobilien
Zielgruppe
WohnKranich, Vermietung und Verwaltung von Immoblien
Aufgabenstellung
Wir haben ganz viele Dokumente, die als PDF erstellt werden sollen, Einheitlich im CI Design, mit Logo etc. Manche PDFS müssen ausfüllbar sein andere sind einfach nur zum Drucken. es sind ca 10-20 Word/PDF Dokumente.

```html
<!DOCTYPE html>
<html lang="de">
<head>
<meta charset="utf-8">
<title>Fragebogen zur Immobilienbewertung – WohnKranich</title>
<link href="https://fonts.googleapis.com/css2?family=Open+Sans:wght@400;600;700&display=swap" rel="stylesheet">
<style>
:root{
  --navy:#0f1f3a;
  --ink:#1c2a44;
  --line:#1f2d4a;
  --paper:#ffffff;
}
*{box-sizing:border-box;margin:0;padding:0}
html,body{width:849px;height:1200px;overflow:hidden;background:var(--paper)}
body{position:relative;font-family:"Open Sans",Arial,sans-serif;color:var(--ink)}
.brand{position:absolute;top:118px;left:0;width:849px;display:flex;justify-content:center;align-items:center;gap:8px}
.brand-mark{width:12px;height:12px;background:var(--navy)}
.brand-name{font-size:20px;font-weight:400;color:var(--navy)}
.title-bar{position:absolute;left:72px;top:187px;width:400px;height:40px;background:var(--navy);color:#fff;font-size:20px;font-weight:400;line-height:40px;padding-left:12px;letter-spacing:.6px}
.box{position:absolute;border:1px solid var(--line)}
.label{position:absolute;left:6px;top:4px;font-size:12.5px;line-height:16px;color:var(--ink)}
.opt{position:absolute;display:flex;align-items:center;gap:6px;font-size:10px;line-height:12px;white-space:nowrap}
.cb{width:16px;height:16px;border:1px solid var(--line);flex:none}
.note{position:absolute;font-size:8px;line-height:12px}
.desc{position:absolute;top:44px;width:228px;font-size:8px;line-height:11.6px;letter-spacing:-.1px}
.small{position:absolute;font-size:10px;line-height:12px}
.band{position:absolute;left:0;top:1175px;width:849px;height:25px}
</style>
</head>
<body>
<header class="brand">
  <span class="brand-mark"></span>
  <span class="brand-name">WohnKranich</span>
</header>

<h1 class="title-bar">Fragebogen zur Immobilienbewertung</h1>

<div class="box" style="left:72px;top:251px;width:235px;height:33px"><span class="label">Vorname</span></div>
<div class="box" style="left:315px;top:251px;width:235px;height:33px"><span class="label">Nachname</span></div>
<div class="box" style="left:558px;top:251px;width:235px;height:33px"></div>

<div class="box" style="left:72px;top:292px;width:235px;height:33px"><span class="label">Telefon</span></div>
<div class="box" style="left:315px;top:292px;width:478px;height:33px"><span class="label">E-Mail-Adresse</span></div>

<div class="box" style="left:72px;top:332px;width:721px;height:33px"><span class="label">Objektadresse</span></div>

<span class="opt" style="left:78px;top:378px"><i class="cb"></i>freistehendes<br>Einfamilienhaus</span>
<span class="opt" style="left:200px;top:382px"><i class="cb"></i>2-Familienhaus</span>
<span class="opt" style="left:315px;top:382px"><i class="cb"></i>Doppelhaushälfte</span>
<span class="opt" style="left:447px;top:382px"><i class="cb"></i>Reihenmittelhaus</span>
<span class="opt" style="left:574px;top:382px"><i class="cb"></i>Reihenendhaus</span>

<span class="opt" style="left:78px;top:428px"><i class="cb"></i>Eigentumswohnung</span>
<span class="opt" style="left:200px;top:428px"><i class="cb"></i>Mehrfamilienhaus</span>
<div class="box" style="left:315px;top:418px;width:235px;height:40px"><span class="label">Anzahl Wohneinheiten</span></div>
<div class="box" style="left:558px;top:418px;width:235px;height:40px"><span class="label">Miteigentum<br>Anteil<span style="margin-left:58px">von</span></span></div>

<div class="box" style="left:72px;top:466px;width:235px;height:33px"><span class="label">Baujahr</span></div>
<div class="box" style="left:315px;top:466px;width:235px;height:33px"><span class="label">Wohnfläche</span></div>
<div class="box" style="left:558px;top:466px;width:235px;height:33px"><span class="label">Grundstücksfläche</span></div>

<section class="box" style="left:72px;top:506px;width:721px;height:93px">
  <span class="label">Modernisierung</span>
  <span class="opt" style="left:6px;top:23px"><i class="cb"></i>Kernsanierung im Jahr:</span>
  <span class="small" style="left:249px;top:26px"><b>oder</b> (Falls eine Teilmodernisierung durchgeführt wurde, kreuzen Sie bitte Zutreffendes an.)</span>
  <span class="opt" style="left:6px;top:48px"><i class="cb"></i>Dach im Jahr:</span>
  <span class="opt" style="left:249px;top:48px"><i class="cb"></i>Leitungen im Jahr:</span>
  <span class="opt" style="left:487px;top:48px"><i class="cb"></i>Dämmung im Jahr:</span>
  <span class="opt" style="left:6px;top:73px"><i class="cb"></i>Fenster im Jahr:</span>
  <span class="opt" style="left:249px;top:73px"><i class="cb"></i>Heizung im Jahr:</span>
  <span class="opt" style="left:487px;top:73px"><i class="cb"></i>Innen im Jahr:</span>
</section>

<section class="box" style="left:72px;top:607px;width:721px;height:119px">
  <span class="label">Ausstattung</span>
  <span class="opt" style="left:6px;top:23px"><i class="cb"></i>einfach</span>
  <span class="opt" style="left:249px;top:23px"><i class="cb"></i>mittel</span>
  <span class="opt" style="left:487px;top:23px"><i class="cb"></i>gehoben</span>
  <p class="desc" style="left:6px">Mauerwerk mit Putz und Anstrich, Holzfenster mit Ein-<br>fachverglasung, einfach Betondachpfannen und keine Wärmedämmung, einfaches Bad mit WC, eine elektri-<br>sche Speicherheizung sowie ein Boiler für Warmwasser</p>
  <p class="desc" style="left:249px;width:232px">Wärmedämmputz, mittlerer Wärmedämmstandard, Kunststofffenster, Rollladen und Isolierverglasung, Be-<br>tondachpfannen sowie eine mittlere Wärmedämmung, 1 Bad mit Dusche und Badewanne sowie ein Gäste-WC, eine Zentralheizung</p>
  <p class="desc" style="left:487px;width:232px">Verblendmauerwerk, Aluminiumfenster, elektr. Rollladen, Wärmeschutz- und/oder Schallschutzverglasung, hoher Wärmedämmstandard, Tondachpfannen oder Schiefer-<br>deckung, Dachausbauten, 1-2 großzügige Bäder sowie ein Gäste-WC, Zentralheizung mit Flachheizkörpern oder Fußbodenheizung, Klimaanlagen, Solaranlagen</p>
</section>

<section class="box" style="left:72px;top:734px;width:721px;height:55px">
  <span class="label">Dachausbau</span>
  <span class="opt" style="left:6px;top:32px"><i class="cb"></i>nicht bekannt</span>
  <span class="opt" style="left:120px;top:32px"><i class="cb"></i>nicht ausgebaut</span>
  <span class="opt" style="left:244px;top:32px"><i class="cb"></i>Flachdach</span>
  <span class="opt" style="left:341px;top:28px"><i class="cb"></i>ausgebautes<br>Dachgeschoss</span>
  <span class="opt" style="left:456px;top:28px"><i class="cb"></i>ausgebauter<br>Spitzboden</span>
  <span class="opt" style="left:564px;top:28px"><i class="cb"></i>ausgebautes<br>Dach u. Spitzboden</span>
</section>

<div class="box" style="left:72px;top:797px;width:356px;height:42px">
  <span class="label">Anzahl Geschosse</span>
  <span class="note" style="left:196px;top:9px">Das (ausgebaute) Dachgeschoss wird<br>nicht als volles Geschoss gerechnet.</span>
</div>
<div class="box" style="left:436px;top:797px;width:357px;height:42px">
  <span class="label">Unterkellert</span>
  <span class="opt" style="left:6px;top:22px"><i class="cb"></i>nicht</span>
  <span class="opt" style="left:91px;top:22px"><i class="cb"></i>zum Teil</span>
  <span class="opt" style="left:198px;top:22px"><i class="cb"></i>voll</span>
</div>

<div class="box" style="left:72px;top:848px;width:356px;height:42px">
  <span class="label">Gesamtzustand des Hauses</span>
  <span class="opt" style="left:6px;top:22px"><i class="cb"></i>gut</span>
  <span class="opt" style="left:77px;top:22px"><i class="cb"></i>mittel</span>
  <span class="opt" style="left:160px;top:22px"><i class="cb"></i>mäßig</span>
</div>
<div class="box" style="left:436px;top:848px;width:357px;height:42px">
  <span class="label">Anzahl Garagen</span>
  <span class="label" style="left:174px">Anzahl Stellplätze</span>
</div>

<div class="box" style="left:72px;top:898px;width:478px;height:43px">
  <span class="label">Erbbaurecht</span>
  <span class="opt" style="left:6px;top:22px"><i class="cb"></i>nein</span>
  <span class="opt" style="left:77px;top:22px"><i class="cb"></i>ja</span>
  <span class="opt" style="left:135px;top:22px"><i class="cb"></i>Bes. Vorbehalte&nbsp; Beginn (Jahr):</span>
  <span class="small" style="left:342px;top:25px">Vertragsablaufjahr:</span>
</div>
<div class="box" style="left:558px;top:898px;width:235px;height:43px"><span class="label">Erbbauzins p.a.</span></div>

<div class="box" style="left:72px;top:950px;width:356px;height:65px">
  <span class="label">Besonderheiten im Grundbuch</span>
  <span class="opt" style="left:6px;top:22px"><i class="cb"></i>Wohnrechte</span>
  <span class="opt" style="left:135px;top:22px"><i class="cb"></i>Wege und Leitungsrechte</span>
  <span class="opt" style="left:6px;top:45px"><i class="cb"></i>Nießbrauchrechte</span>
  <span class="opt" style="left:135px;top:45px"><i class="cb"></i>keine</span>
</div>
<div class="box" style="left:436px;top:950px;width:357px;height:65px">
  <span class="label">Mieteinnahmen</span>
  <span class="opt" style="left:6px;top:22px"><i class="cb"></i>nein</span>
  <span class="opt" style="left:91px;top:22px"><i class="cb"></i>ja, Kaltmiete pro Monat:</span>
</div>

<div class="box" style="left:72px;top:1023px;width:721px;height:75px"><span class="label">Notizen/Hinweise</span></div>

<div class="box" style="left:72px;top:1106px;width:356px;height:40px">
  <span class="label">Anzahl Objektbilder</span>
  <span class="small" style="left:230px;top:7px">(Fotos bitte beschriften.)</span>
</div>
<div class="box" style="left:436px;top:1106px;width:357px;height:40px"><span class="label">Unterschrift</span></div>

<svg class="band" viewBox="0 0 849 25" aria-hidden="true">
  <rect width="849" height="25" fill="#0f1f3a"/>
  <polygon points="643,0 652,0 643,25 634,25" fill="#ffffff"/>
</svg>
</body>
</html>
```